Brevik Fabrication - Business Card Design

We would like a dark (likely black) themed business card to be able to hand out to potential clients. We may list our services on the card or keep it clean. Unsure. Logo attached

```html
<!DOCTYPE html>
<html lang="en">
<head>
<meta charset="UTF-8">
<title>Brevik Fabrication – Business Card</title>
<link href="https://fonts.googleapis.com/css2?family=Roboto:wght@400;500;700&display=swap" rel="stylesheet">
<style>
  :root {
    --backdrop: #cdd3d3;
    --card: #0b0b0c;
    --card-edge: #e03a1c;
    --accent-red: #e4431f;
    --accent-blue: #1f4fc4;
    --text-blue: #2553b8;
  }
  * { box-sizing: border-box; margin: 0; padding: 0; }
  html, body {
    width: 1200px; height: 1200px; overflow: hidden;
    background: var(--backdrop);
    font-family: "Roboto", Arial, sans-serif;
  }
  .canvas {
    position: relative; width: 1200px; height: 1200px;
  }
  .card {
    position: absolute; left: 150px; width: 900px; height: 514px;
    background: var(--card);
    border-bottom: 6px solid var(--card-edge);
    box-shadow: 0 18px 40px rgba(0,0,0,0.25);
  }
  .card--front { top: 60px; }
  .card--back { top: 626px; }

  .holder { position: absolute; left: 64px; top: 110px; }
  .holder__name {
    color: var(--accent-red); font-size: 34px; font-weight: 500; letter-spacing: 1px;
  }
  .holder__role {
    color: var(--text-blue); font-size: 24px; margin-top: 6px;
  }
  .divider {
    position: absolute; left: 64px; top: 212px; width: 740px; height: 2px;
    background: var(--accent-blue);
  }
  .contacts {
    position: absolute; left: 64px; top: 240px; list-style: none;
  }
  .contacts li {
    display: flex; align-items: center; gap: 14px;
    color: var(--text-blue); font-size: 24px; line-height: 38px;
  }
  .contacts svg { width: 20px; height: 20px; flex: none; }

  .wordmark {
    position: absolute; display: flex; align-items: center; gap: 16px;
    color: var(--accent-blue); font-weight: 700; text-transform: uppercase;
  }
  .wordmark__dot { border-radius: 50%; background: var(--accent-red); flex: none; }
  .card--front .wordmark { right: 64px; top: 100px; font-size: 40px; }
  .card--front .wordmark__dot { width: 44px; height: 44px; }

  .address {
    position: absolute; right: 96px; bottom: 60px; text-align: right;
    color: var(--text-blue); font-size: 24px; line-height: 32px;
  }

  .card--back .wordmark { right: 70px; bottom: 90px; font-size: 56px; }
  .card--back .wordmark__dot { width: 64px; height: 64px; }
</style>
</head>
<body>
<main class="canvas">
  <section class="card card--front" aria-label="Card front">
    <div class="holder">
      <h1 class="holder__name">DANIEL HARROW</h1>
      <p class="holder__role">Manager</p>
    </div>
    <div class="wordmark"><span class="wordmark__dot"></span>Brevik Fabrication</div>
    <div class="divider"></div>
    <ul class="contacts">
      <li>
        <svg viewBox="0 0 24 24" fill="none" stroke="var(--accent-red)" stroke-width="2.2" stroke-linecap="round" stroke-linejoin="round"><path d="M5 3h4l2 5-2.5 1.5a11 11 0 0 0 6 6L16 13l5 2v4a2 2 0 0 1-2 2A16 16 0 0 1 3 5a2 2 0 0 1 2-2z"/></svg>
        555-014-2100
      </li>
      <li>
        <svg viewBox="0 0 24 24" fill="none" stroke="var(--accent-red)" stroke-width="2.2" stroke-linejoin="round"><rect x="3" y="5" width="18" height="14" rx="1"/><path d="M3 6l9 7 9-7"/></svg>
        hello@brevikfab.com
      </li>
      <li>
        <svg viewBox="0 0 24 24" fill="none" stroke="var(--accent-red)" stroke-width="2.2"><circle cx="12" cy="12" r="9"/><path d="M3 12h18M12 3c3 3 3 15 0 18M12 3c-3 3-3 15 0 18"/></svg>
        www.brevikfab.com
      </li>
    </ul>
    <p class="address">Your address, city<br>state, ZIP 0000</p>
  </section>

  <section class="card card--back" aria-label="Card back">
    <div class="wordmark"><span class="wordmark__dot"></span>Brevik Fabrication</div>
  </section>
</main>
</body>
</html>
```